Jewelry store needs fully functional Ecommerce website

Web Design Brief for our E-commerce Jewelry retail store.
Description

We need a fully coded Shopify website. The Shopify site will need to be fully functional with an Ecommerce integration (fully integrated with Paypal and All other gateways) and will need to be SEO optimized.
We sell jewelry items like: rings, earrings, necklaces etc. The website should have an elegant, modern, professional, fun, look.

***We would like the website to look and function similarly to this website:
https://velvorisco.com

Color Preference
Colors to be used are white background with black font and light pink/ purple/ gold tints. We have attached our logo as reference.

Functionalities
The store will function like a typical Ecommerce jewelry store, using the products/categories as the starting page. Going into individual product pages by selecting images and leading to a detailed “buy now” page for the selected product.

Target Market
Jewelry lovers.

Should Not Have:
- - Dull and common design
- - Messy/unstructured navigation

Coded - Design and coding required
Target Audience are women from 16-50 years old.
We will need to be able to add products and make modifications to the website as needed.

We need the following apps installed and Operating:
-Tally Shift; Order Look Up (rename “track your order”) ; Help Center (Questions and Answers) ; Pemmo Reviews; TXT Nudge; Drenoza Email Marketing ; Plivet (Facebook messenger bump) ; Vantro multi- currency (translate currency to buyer) ; Discounted Upsell ; Easy Contact form App
We will need all products imported: (below is information for importing products). We will provide all links that serve entire active item product catalog in shopifys import format:
DataFeed:

If you are getting started with Shopify, a combination of the Shopify Import Format and XML feeds is ideal. The Shopify Import Format will output a file that can be uploaded into Shopify’s product database. After you import, you can use the XML feed and a third party app to keep the inventory up to date in real time, take down items that go out of stock etc., all without regular human intervention. There a several Shopify apps that can do this type of feed integration. We have had a good experience with Tally Shift, which is an app that can be configured to accept our XML feed and update products on a set schedule. You can even set your own margins based on our wholesale price with this app.

Shopify Formatted HTML TableTo make it easier to get started on Shopify, we included a format that outputs the required fields for a product import in Shopify. In order to use the embedded Excel file, first open the file (Auto-Shopify-Datasheet-Format.xslx), Refresh it (under Data tab), and then Save As with a new file name in a CSV (UTF-8) file. That file can then be split into smaller CSV files (if there is a limit on the number of products per file) for import into Shopify.

Target Market(s)

Jewelry Lovers

Industry/Entity Type

Jewelry Store

Coding

Number of Pages Required

5+ page

Colors
eda3c7
d3a5cc
ffffff

Requirements
Must have
• Color Preference
Colors to be used are white background with black font and light pink/ purple/ gold tints.

https://velvorisco.com
Should not have
• Should Not Have:

```html
<!DOCTYPE html>
<html lang="en">
<head>
<meta charset="utf-8">
<title>Jewelry Collection</title>
<link rel="stylesheet" href="https://fonts.googleapis.com/css2?family=Josefin+Sans:wght@400;600;700&family=Questrial&display=swap">
<style>
:root{
  --gold:#cc9933;
  --gold-text:#c8952f;
  --ink:#111111;
  --navy:#10294a;
  --muted:#8f8f8f;
  --hero-bg:#f1f1f1;
  --card-grey:#ececec;
  --band-bg:#f4f7f9;
  --peach:#f7e2c8;
  --peach-dark:#f3d6b4;
  --story-bg:#f5f3f3;
  --news-bg:#e2e2e4;
  --footer-bg:#f7f7f7;
  --white:#ffffff;
}
*{margin:0;padding:0;box-sizing:border-box}
html,body{width:1200px;height:2914px;overflow:hidden;background:var(--white)}
body{font-family:"Questrial",sans-serif;color:var(--ink);position:relative}
.head{font-family:"Josefin Sans",sans-serif;font-weight:700;letter-spacing:1px;text-transform:uppercase}
section{position:absolute;left:0;width:1200px;overflow:hidden}
.abs{position:absolute}
.btn{position:absolute;display:inline-block;border:2px solid var(--ink);font-family:"Josefin Sans",sans-serif;font-weight:600;font-size:16px;letter-spacing:1px;padding:11px 12px 7px;text-transform:uppercase;color:var(--ink);text-decoration:none;background:transparent}
.btn.light{border-color:#fff;color:#fff}
.placeholder{position:absolute}

/* hero */
.hero{top:0;height:629px;background:var(--hero-bg)}
.hero .menu{left:86px;top:19px}
.hero .logo{left:85px;top:74px;font-size:41px;letter-spacing:2px}
.hero .social{right:92px;top:16px;display:flex;gap:12px}
.hero .social span{width:14px;height:14px;border-radius:50%;background:#333}
.hero .price{left:89px;top:273px;font-size:43px;color:var(--gold-text)}
.hero .title{left:89px;top:322px;font-size:44px;color:var(--ink)}
.hero .lede{left:89px;top:378px;width:420px;font-size:15px;line-height:21px;color:#222}
.hero .btn{left:87px;top:458px}
.hero .photo{left:475px;top:0;width:725px;height:629px;background:radial-gradient(circle at 55% 40%,#d9ddd9 0,#d9ddd9 46%,transparent 46.3%),linear-gradient(135deg,#e8d2c0 0%,#d9b196 45%,#c99a79 80%,#efe7df 100%)}

/* category cards */
.cards{top:629px;height:385px;display:flex}
.card{position:relative;height:385px;text-align:center}
.card .img{position:absolute;left:50%;transform:translateX(-50%);top:48px;width:200px;height:170px;border-radius:6px}
.card h3{position:absolute;left:0;right:0;top:228px;font-size:17px;letter-spacing:1.2px}
.card p{position:absolute;left:50%;transform:translateX(-50%);top:257px;width:290px;font-size:13.5px;line-height:17px;color:var(--muted)}
.card .btn{left:50%;transform:translateX(-50%);top:323px}
.card.c1{width:394px;background:var(--card-grey)}
.card.c2{width:411px;background:var(--gold)}
.card.c2 h3,.card.c2 p{color:#fff}
.card.c3{width:395px;background:var(--card-grey)}
.c1 .img{background:linear-gradient(160deg,#6b5bc7,#d9d9dd 60%)}
.c2 .img{width:250px;background:linear-gradient(160deg,#f3f3f3,#bdbdbd)}
.c3 .img{background:linear-gradient(160deg,#4b46b8,#d7d7dd 70%)}

/* women's bands */
.bands{top:1014px;height:400px;background:var(--band-bg)}
.bands h2{left:97px;top:133px;font-size:26px;letter-spacing:1.6px}
.bands p{left:97px;top:175px;width:310px;font-size:15px;line-height:20.5px}
.bands .btn{left:97px;top:257px}
.bands .photo{left:600px;top:0;width:600px;height:400px;background:linear-gradient(120deg,#f7f2e4 0%,#e2c05a 35%,#f4f4f4 60%,#e6c25e 80%,#f4f6f8 100%)}

/* couples */
.couples{top:1414px;height:402px;background:var(--peach)}
.couples .kicker{left:96px;top:40px;font-family:"Josefin Sans",sans-serif;font-size:21px;letter-spacing:1.2px;text-transform:uppercase}
.couples .kicker b{color:var(--navy)}
.couples .rings{left:86px;top:97px;width:280px;height:230px;background:linear-gradient(150deg,#f6ecdf,#cfcfcf 45%,#9f9f9f 70%,#f4e4cf)}
.couples .design{left:395px;top:152px;width:310px;text-align:center;font-family:"Josefin Sans",sans-serif}
.couples .design .l1{font-size:27px;letter-spacing:1.6px;text-transform:uppercase}
.couples .design .l2{font-size:32px;font-weight:700;letter-spacing:1.6px;text-transform:uppercase;margin-top:2px}
.couples .btn{left:478px;top:248px}
.promo{position:absolute;left:731px;top:0;width:469px;height:402px;background:var(--gold);color:#fff;text-align:center}
.promo .arrows{position:absolute;left:15px;top:21px;display:flex;gap:5px}
.promo .arrows span{width:34px;height:33px;border:1px solid #fff;border-radius:4px;display:flex;align-items:center;justify-content:center}
.promo .ring{position:absolute;left:130px;top:50px;width:190px;height:160px;background:linear-gradient(160deg,#f7f7f7,#c9c9c9);border-radius:6px}
.promo h3{position:absolute;left:0;right:0;top:237px;font-size:20px}
.promo p{position:absolute;left:50%;transform:translateX(-50%);top:264px;width:300px;font-size:15px;line-height:17px}
.promo .cost{position:absolute;left:0;right:0;top:336px;font-family:"Josefin Sans",sans-serif;font-weight:700;font-size:32px}

/* stories */
.stories{top:1816px;height:409px;background:var(--story-bg)}
.stories .lead{left:60px;top:110px;width:540px;text-align:center;font-size:22px;line-height:25px;color:#222}
.stories .quote{left:110px;top:196px;width:440px;text-align:center;font-size:17px;line-height:17px;color:#333}
.stories .qo{left:112px;top:188px;font-size:30px;color:#444}
.stories .qc{left:445px;top:218px;font-size:30px;color:#444}
.stories .cite{left:60px;top:262px;width:540px;text-align:center;font-size:12px;color:var(--muted)}
.stories .read{left:60px;top:312px;width:519px;text-align:center;font-size:12px;color:#333;text-decoration:underline}
.stories .photo{left:631px;top:0;width:569px;height:409px;background:linear-gradient(135deg,#d4a98b 0%,#e3c7b4 40%,#f0ebe7 70%,#d9b39a 100%)}

/* features */
.features{top:2225px;height:215px;background:var(--white)}
.feature{position:absolute;top:48px;width:330px;height:100px}
.feature .badge{position:absolute;left:0;top:0;width:85px;height:85px;border-radius:50%;background:var(--peach);display:flex;align-items:center;justify-content:center}
.feature h4{position:absolute;left:100px;top:11px;font-size:16px;letter-spacing:1px}
.feature p{position:absolute;left:100px;top:35px;width:210px;font-size:12.5px;line-height:17px;color:var(--muted)}
.f1{left:86px}.f2{left:441px}.f3{left:791px}

/* newsletter */
.newsletter{top:2440px;height:72px;background:var(--news-bg)}
.newsletter .label{left:148px;top:28px;font-size:16px;letter-spacing:.6px;text-transform:uppercase;color:#222}
.newsletter .field{left:410px;top:17px;width:425px;height:38px;background:#fff;border:1px solid #ddd;font-size:15px;color:#aaa;padding:11px 14px}
.newsletter .submit{left:854px;top:17px;width:164px;height:38px;background:var(--navy);color:#fff;font-size:16px;letter-spacing:.6px;text-transform:uppercase;text-align:center;padding-top:11px}

/* footer */
.footer{top:2512px;height:402px;background:var(--footer-bg)}
.col{position:absolute;top:44px}
.col h5{font-family:"Josefin Sans",sans-serif;font-weight:700;font-size:12px;letter-spacing:.5px;color:var(--navy);margin-bottom:13px}
.col li{list-style:none;font-size:12px;line-height:20.5px;color:#555;text-transform:uppercase}
.col1{left:104px}.col2{left:344px}.col3{left:614px}.col4{left:904px}
.follow{position:absolute;left:95px;top:252px;display:flex;gap:12px}
.follow span{width:26px;height:26px;border-radius:50%}
.pay{position:absolute;left:725px;top:250px;display:flex;gap:6px}
.pay span{width:43px;height:28px;border-radius:4px;background:#c9c9c9}
.pay .seal{width:106px;background:#fff;border:1px solid #bbb;margin-left:14px}
.legal{position:absolute;left:0;right:0;top:311px;text-align:center;font-size:12px;line-height:18.5px;color:#333}
.legal b{display:block;font-size:12px}
</style>
</head>
<body>

<section class="hero">
  <svg class="abs menu" width="22" height="14" viewBox="0 0 22 14"><path d="M0 1h22M0 7h22M0 13h22" stroke="#111" stroke-width="2"/></svg>
  <div class="abs head logo">Your Logo</div>
  <div class="abs social" aria-label="Social links"><span></span><span></span><span></span><span></span><span></span></div>
  <div class="placeholder photo" role="img" aria-label="Portrait of a woman wearing gold rings and necklaces"></div>
  <div class="abs head price">From $299</div>
  <div class="abs head title">Jewelry Collection</div>
  <p class="abs lede">Aenean sollicitudin, lorem quis bibendum auctor, nisi elit consequat ipsum, nec sagittis sem nibh id elit. Duis sed odio sit amet nibh</p>
  <a class="btn" href="#">Shop Now</a>
</section>

<section class="cards">
  <div class="card c1">
    <div class="img" role="img" aria-label="Silver engagement ring with purple stone"></div>
    <h3 class="head">Heirloom Engagement Rings</h3>
    <p>Accordingly composed pictures in which contrived to get as many lines as possible leading inward</p>
    <a class="btn" href="#">Learn More</a>
  </div>
  <div class="card c2">
    <div class="img" role="img" aria-label="Three diamond wedding band rings"></div>
    <h3 class="head">Heirloom Wedding Bands</h3>
    <p>Accordingly composed pictures in which contrived to get as many lines as possible leading inward</p>
    <a class="btn light" href="#">Learn More</a>
  </div>
  <div class="card c3">
    <div class="img" role="img" aria-label="Purple sapphire ring with diamond halo"></div>
    <h3 class="head">Heirloom Fine Jewelry</h3>
    <p>Accordingly composed pictures in which contrived to get as many lines as possible leading inward</p>
    <a class="btn" href="#">Learn More</a>
  </div>
</section>

<section class="bands">
  <h2 class="abs head">Women’s Wedding Bands</h2>
  <p class="abs">Accordingly composed pictures in which contrived to get as many lines as possible leading inward</p>
  <a class="btn" href="#">Shop Now</a>
  <div class="placeholder photo" role="img" aria-label="Gold crown ornament and gold and silver heart pendant"></div>
</section>

<section class="couples">
  <div class="abs kicker">150,000 Happy <b>Couples</b> &amp; Counting</div>
  <div class="placeholder rings" role="img" aria-label="Pair of pavé diamond wedding rings"></div>
  <div class="abs design"><div class="l1">Design Your Own</div><div class="l2">Engagement Ring</div></div>
  <a class="btn" href="#">Shop Now</a>
  <div class="promo">
    <div class="arrows">
      <span><svg width="10" height="14" viewBox="0 0 10 14"><path d="M8 1L2 7l6 6" stroke="#fff" stroke-width="1.5" fill="none"/></svg></span>
      <span><svg width="10" height="14" viewBox="0 0 10 14"><path d="M2 1l6 6-6 6" stroke="#fff" stroke-width="1.5" fill="none"/></svg></span>
    </div>
    <div class="ring" role="img" aria-label="Diamond engagement ring set"></div>
    <h3 class="head">Lorem Collections</h3>
    <p>Accordingly composed pictures in which contrived to get as many lines as possible leading inward</p>
    <div class="cost">$ 299</div>
  </div>
</section>

<section class="stories">
  <p class="abs lead">View our customers' engagement moments from around the world</p>
  <span class="abs qo">“</span>
  <p class="abs quote">...Eventually, we came upon a secluded gazebo, and the rest was history...</p>
  <span class="abs qc">”</span>
  <p class="abs cite">- Delia Fenwick (California, US)</p>
  <a class="abs read" href="#">READ THE STORIES</a>
  <div class="placeholder photo" role="img" aria-label="Joyful woman holding a small gift box with a pink ribbon"></div>
</section>

<section class="features">
  <div class="feature f1">
    <div class="badge"><svg width="40" height="46" viewBox="0 0 40 46" fill="none" stroke="#555" stroke-width="1.6"><path d="M20 2C9 2 3 10 3 18c0 6 6 11 13 14h8c7-3 13-8 13-14C37 10 31 2 20 2z"/><path d="M20 2c-5 4-7 10-7 16s2 10 3 14M20 2c5 4 7 10 7 16s-2 10-3 14"/><path d="M16 32l1 6h6l1-6M17 38h6v5h-6z"/></svg></div>
    <h4 class="head">Free Shipping</h4>
    <p>But from the first I was disap-pointed with it. In about a week I was tired of seeing sights</p>
  </div>
  <div class="feature f2">
    <div class="badge"><svg width="46" height="38" viewBox="0 0 46 38" fill="none" stroke="#555" stroke-width="1.6"><rect x="2" y="9" width="40" height="27" rx="3"/><path d="M6 9l22-7 4 7M30 18h12v10H30z"/><circle cx="35" cy="23" r="1.8"/></svg></div>
    <h4 class="head">Refund Option</h4>
    <p>I had no real pal to go about with, which probably explains things. Plenty of people invited me</p>
  </div>
  <div class="feature f3">
    <div class="badge"><svg width="46" height="46" viewBox="0 0 46 46" fill="none" stroke="#555" stroke-width="1.6"><ellipse cx="23" cy="23" rx="20" ry="8"/><ellipse cx="23" cy="23" rx="20" ry="8" transform="rotate(60 23 23)"/><ellipse cx="23" cy="23" rx="20" ry="8" transform="rotate(-60 23 23)"/><circle cx="23" cy="23" r="3"/></svg></div>
    <h4 class="head">Payment Options</h4>
    <p>They would fling me a question or two about South Africa, and then get on their own affairs</p>
  </div>
</section>

<section class="newsletter">
  <div class="abs label">Sign up for our newsletter</div>
  <div class="abs field">Enter Your Email</div>
  <div class="abs submit">Subscribe Now</div>
</section>

<section class="footer">
  <div class="col col1"><h5>OUR COMPANY</h5><ul><li>About Us</li><li>Our Showroom</li><li>Directions</li><li>Hours of Operation</li><li>Member Accounts</li><li>Contact Us</li></ul></div>
  <div class="col col2"><h5>OUR PRINCIPLES</h5><ul><li>Customer Satisfaction</li><li>Unbeatable Prices</li><li>Return Policy</li><li>Warranty</li><li>Information Policy</li></ul></div>
  <div class="col col3"><h5>OUR SPECIALTIES</h5><ul><li>Diamond Brokerage</li><li>Engagement Rings</li><li>Women's Wedding Bands</li><li>Men's Wedding Bands</li><li>Bracelets</li><li>Earrings</li><li>Pendants</li></ul></div>
  <div class="col col4"><h5>OUR SERVICES</h5><ul><li>Education</li><li>Consultation</li><li>Appraisals</li><li>Sales &amp; Consignments</li><li>Insurance</li><li>Jewelry Repair</li></ul></div>
  <div class="follow" aria-label="Follow us">
    <span style="background:#3b5aa0"></span><span style="background:#e0533f"></span><span style="background:#2aa3ef"></span><span style="background:#e5344b"></span><span style="background:#d8232a"></span><span style="background:#cf2e36"></span>
  </div>
  <div class="pay" aria-label="Accepted payments"><span></span><span></span><span></span><span></span><span></span><span class="seal"></span></div>
  <div class="legal">
    <b>Orlen Marsh</b>
    At Orlen Marsh Inc., buying an engagement ring or wedding band will be a positive piece of the story of your love.<br>
    Get the information you need to find and select the stunning antique, vintage, or replica engagement ring of your sweetheart's dreams.<br>
    Copyright © 1999-2017 Orlen Marsh Inc. All rights reserved.
  </div>
</section>

</body>
</html>
```